'Brantley e@sy' Initial leaflet

I need an A5 Leaflet designed to launch the new service we are offering.
Currently we operate a traditional estate agency based in the uk that covers sales and letting of property.

The working name for the new service is 'Brantley e@sy'

We are starting a new offering that will be an online offering for the local area. Similar to 'Tallowgate' but with an actual local face and office.
I need the leaflet to promote this.
The leaflet must be modern, informative and in our corporate colours. I have attached some logos and previous leaflets that we have had to show colours etc.
The main points to detail on the leaflet will be that
we offer an Online Service
Its a lower price
We still offer the local office/face.
Professional Photos Included
Floorplans Included

The price we will offer this service at will be 'From £795 inc VAT'

Id like to have an offer on the leaflet that instruction received in September/October 2018 will get the service for reduced price of £600 Including VAT.

I look forward to seeing what we get!

Martin

Requirements
Must have
• Must be double sided! Should be attractive and modern.

```html
<!DOCTYPE html>
<html lang="en">
<head>
<meta charset="utf-8">
<title>Brantley e@sy – A5 leaflet, front and back</title>
<link rel="stylesheet" href="https://fonts.googleapis.com/css2?family=Lato:wght@400;700;900&display=swap">
<style>
  :root {
    --orange: #f15a3a;
    --black: #1a0d0d;
    --white: #ffffff;
    --ink: #1c1c1c;
    --yellow: #ffe21a;
    --board: #a9a9a9;
    --photo-green: #6f9a3a;
    --photo-sky: #b9c27a;
    --photo-grey: #c9ccd2;
  }
  html, body {
    margin: 0;
    padding: 0;
    width: 1200px;
    height: 1200px;
    overflow: hidden;
    background: var(--board);
  }
  .board {
    position: relative;
    width: 1200px;
    height: 1200px;
  }
  .brand-mark {
    position: absolute;
    left: 534px;
    top: 40px;
    width: 132px;
    height: 132px;
  }
  .leaflet {
    position: absolute;
    top: 267px;
    width: 543px;
    height: 768px;
    box-shadow: 0 6px 18px rgba(0,0,0,0.35);
  }
  .leaflet--front { left: 42px; }
  .leaflet--back  { left: 613px; }
  .leaflet svg { display: block; width: 543px; height: 768px; }

  .sans   { font-family: 'Lato', sans-serif; }
  .bold   { font-weight: 700; }
  .heavy  { font-weight: 900; }
  .fill-orange { fill: var(--orange); }
  .fill-black  { fill: var(--black); }
  .fill-white  { fill: var(--white); }
  .fill-ink    { fill: var(--ink); }
  .fill-yellow { fill: var(--yellow); }
</style>
</head>
<body>
<main class="board">

  <!-- Brand roundel above the spread -->
  <svg class="brand-mark" viewBox="0 0 132 132" aria-label="Brantley">
    <circle cx="66" cy="66" r="63" fill="var(--orange)" stroke="var(--black)" stroke-width="4"/>
    <text x="66" y="74" text-anchor="middle" class="sans bold fill-black" font-size="22">Brantley</text>
  </svg>

  <!-- FRONT -->
  <section class="leaflet leaflet--front">
    <svg viewBox="0 0 588 832">
      <defs>
        <linearGradient id="aerialTones" x1="0" y1="0" x2="1" y2="1">
          <stop offset="0" stop-color="var(--photo-sky)"/>
          <stop offset="1" stop-color="var(--photo-green)"/>
        </linearGradient>
        <clipPath id="frontClip"><rect width="588" height="832"/></clipPath>
      </defs>
      <g clip-path="url(#frontClip)">
        <rect class="background" width="588" height="832" fill="var(--orange)"/>

        <!-- top-left black swoosh -->
        <path class="swoosh" d="M52 0 H120 C90 150 50 300 0 430 V230 C25 150 42 70 52 0 Z" fill="var(--black)"/>

        <!-- black band behind the brand name -->
        <path class="band" d="M30 280 C180 370 400 350 588 300 V410 C430 460 300 470 190 462 C110 456 50 410 30 280 Z" fill="var(--black)"/>

        <!-- white content panel -->
        <path class="content-panel" d="M588 410 C430 460 300 472 200 466 C130 476 90 540 70 610 C55 670 35 730 0 769 H588 Z" fill="var(--white)"/>

        <!-- hero aerial photo -->
        <circle cx="384" cy="56" r="228" fill="var(--white)"/>
        <circle cx="384" cy="56" r="215" fill="url(#aerialTones)" role="img" aria-label="Aerial photograph of a large detached house with lawns and a curving driveway"/>

        <!-- brand circle -->
        <circle cx="129" cy="311" r="100" fill="var(--white)"/>
        <circle cx="129" cy="311" r="88" fill="var(--orange)" stroke="var(--black)" stroke-width="4"/>

        <text x="276" y="400" class="sans bold fill-orange" font-size="44">Brantley</text>
        <text x="372" y="418" class="sans bold fill-white" font-size="10">Estate Agents</text>

        <!-- price badge -->
        <circle cx="65" cy="477" r="57" fill="var(--black)" stroke="var(--white)" stroke-width="4"/>
        <text x="65" y="462" text-anchor="middle" class="sans bold fill-white" font-size="20">From</text>
        <text x="65" y="484" text-anchor="middle" class="sans heavy fill-yellow" font-size="21">£795</text>
        <text x="65" y="506" text-anchor="middle" class="sans bold fill-white" font-size="19">Incl. VAT</text>

        <text x="558" y="494" text-anchor="end" class="sans heavy fill-orange" font-size="26">A new service just launched!</text>

        <!-- service name band -->
        <rect x="245" y="508" width="380" height="61" rx="30" fill="var(--orange)"/>
        <text x="412" y="552" text-anchor="middle" class="sans heavy fill-white" font-size="36">Brantley e@sy</text>

        <g class="intro sans fill-ink" font-size="15.5">
          <text x="98" y="598">We are starting <tspan class="bold">an online offering</tspan> for the local area, similar to</text>
          <text x="98" y="615">‘Tallowgate’ - with an actual local face and office.</text>
          <text x="98" y="631">We still offer the local office/face as usual.</text>
        </g>

        <g class="benefits">
          <g transform="translate(126 642)">
            <rect x="0" y="3" width="15" height="15" fill="none" stroke="var(--orange)" stroke-width="2"/>
            <path d="M3 10 L7 15 L17 0" fill="none" stroke="var(--orange)" stroke-width="3"/>
          </g>
          <g transform="translate(126 665)">
            <rect x="0" y="3" width="15" height="15" fill="none" stroke="var(--orange)" stroke-width="2"/>
            <path d="M3 10 L7 15 L17 0" fill="none" stroke="var(--orange)" stroke-width="3"/>
          </g>
          <g transform="translate(126 688)">
            <rect x="0" y="3" width="15" height="15" fill="none" stroke="var(--orange)" stroke-width="2"/>
            <path d="M3 10 L7 15 L17 0" fill="none" stroke="var(--orange)" stroke-width="3"/>
          </g>
          <g class="sans bold fill-orange" font-size="18.5">
            <text x="159" y="658">Lower Price</text>
            <text x="159" y="681">Professional Photos Included</text>
            <text x="159" y="704">Floorplan Included</text>
          </g>
        </g>

        <g class="offer sans fill-ink" font-size="15.5">
          <text x="95" y="731">Instruction received in September/October 2018 will get the</text>
          <text x="95" y="749">service price <tspan class="bold">reduced by £600 including VAT</tspan></text>
        </g>

        <!-- footer -->
        <rect y="761" width="588" height="8" fill="var(--orange)"/>
        <rect y="769" width="588" height="63" fill="var(--black)"/>
        <circle cx="42" cy="801" r="24" fill="var(--orange)" stroke="var(--white)" stroke-width="2"/>
        <text x="76" y="810" class="sans bold fill-orange" font-size="30">Brantley</text>
        <text x="140" y="824" class="sans bold fill-white" font-size="8">Estate Agents</text>

        <path d="M302 782 c-2 2 -2 6 2 10 l3 3 c4 4 8 4 10 2 l2 -2 -4 -4 -2 2 c-2 -1 -5 -4 -6 -6 l2 -2 -4 -4 z" fill="var(--orange)"/>
        <text x="325" y="796" class="sans heavy fill-white" font-size="18">01632 960418</text>
        <g transform="translate(309 810)" fill="none" stroke="var(--orange)" stroke-width="1.6">
          <circle r="7"/>
          <ellipse rx="3" ry="7"/>
          <line x1="-7" y1="0" x2="7" y2="0"/>
        </g>
        <text x="325" y="816" class="sans heavy fill-white" font-size="18">brantleyestateagents.co.uk</text>
      </g>
    </svg>
  </section>

  <!-- BACK -->
  <section class="leaflet leaflet--back">
    <svg viewBox="0 0 588 832">
      <defs>
        <linearGradient id="keysTones" x1="0" y1="0" x2="1" y2="1">
          <stop offset="0" stop-color="#e6e2dc"/>
          <stop offset="1" stop-color="#b9a79a"/>
        </linearGradient>
        <linearGradient id="planTones" x1="0" y1="0" x2="1" y2="1">
          <stop offset="0" stop-color="#8f959c"/>
          <stop offset="1" stop-color="#4c5058"/>
        </linearGradient>
        <linearGradient id="gemTones" x1="0" y1="0" x2="1" y2="1">
          <stop offset="0" stop-color="#eef0f3"/>
          <stop offset="1" stop-color="var(--photo-grey)"/>
        </linearGradient>
        <clipPath id="backClip"><rect width="588" height="832"/></clipPath>
      </defs>
      <g clip-path="url(#backClip)">
        <rect class="background" width="588" height="832" fill="var(--white)"/>

        <!-- header swoosh -->
        <path d="M0 0 H588 V52 C400 42 200 72 0 112 Z" fill="var(--orange)"/>
        <path d="M0 112 C200 72 400 42 588 52 V80 C400 90 200 150 0 192 Z" fill="var(--black)"/>
        <path d="M0 192 C200 150 400 90 588 80 V92 C400 102 200 166 0 208 Z" fill="var(--orange)"/>
        <text class="sans heavy fill-white" font-size="36" transform="translate(16 158) rotate(-17)">Our Services</text>

        <circle cx="341" cy="156" r="30" fill="var(--orange)" stroke="var(--black)" stroke-width="3"/>
        <text x="384" y="168" class="sans bold fill-orange" font-size="42">Brantley</text>
        <text x="490" y="184" class="sans bold fill-ink" font-size="9">Estate Agents</text>

        <g class="intro sans fill-ink" font-size="15.5">
          <text x="117" y="216"><tspan class="bold fill-orange">Brantley Estate Agents</tspan> specialise in residential sales, lettings,</text>
          <text x="117" y="233">and property management.  Our experienced team can advise</text>
          <text x="117" y="250">you on just about everything from decor to financial advice,</text>
          <text x="117" y="267">we have it covered!</text>
        </g>

        <!-- services column -->
        <rect x="-20" y="289" width="226" height="32" rx="16" fill="var(--orange)"/>
        <text x="17" y="314" class="sans heavy fill-white" font-size="22">Sales</text>
        <g class="sans fill-ink" font-size="14.5">
          <text x="16" y="340">All our properties benefit from our</text>
          <text x="16" y="356">full marketing package, this includes:</text>
        </g>
        <g class="sans bold fill-orange" font-size="14.5">
          <text x="16" y="385">● Floorplan</text>
          <text x="16" y="401">● Professionally Enhanced Photography</text>
          <text x="16" y="416">● Video Tour</text>
          <text x="16" y="432">● Branded Literature</text>
        </g>

        <rect x="-20" y="448" width="226" height="33" rx="16" fill="var(--orange)"/>
        <text x="17" y="473" class="sans heavy fill-white" font-size="22">Lettings</text>
        <g class="sans bold fill-orange" font-size="14.5">
          <text x="16" y="504">● Let Only</text>
          <text x="16" y="519">● Gold Management</text>
          <text x="16" y="535">● Diamond Management</text>
        </g>

        <rect x="-20" y="553" width="226" height="33" rx="16" fill="var(--orange)"/>
        <text x="17" y="578" class="sans heavy fill-white" font-size="22">Others</text>
        <g class="sans bold fill-orange" font-size="14.5">
          <text x="16" y="605">● Financial Services</text>
          <text x="16" y="620">● Solicitors</text>
          <text x="16" y="636">● Extras</text>
        </g>
        <g class="sans fill-ink" font-size="14.2">
          <text x="16" y="659">We also provide any other property</text>
          <text x="16" y="675">service required including but not limited</text>
          <text x="16" y="690">to <tspan class="bold">Energy Performance Certificate,</tspan></text>
          <text x="16" y="706" class="bold">Landlord Gas Safety Certificates, EICR</text>
          <text x="16" y="721" class="bold">Reports, and Phto Inventories.</text>
        </g>

        <line x1="301" y1="289" x2="301" y2="781" stroke="var(--orange)" stroke-width="3"/>

        <!-- contact column -->
        <rect x="321" y="289" width="300" height="32" rx="16" fill="var(--black)"/>
        <text x="340" y="313" class="sans heavy fill-white" font-size="22">Contact Us</text>

        <path d="M330 340 a7 7 0 0 1 7 7 c0 5 -7 12 -7 12 s-7 -7 -7 -12 a7 7 0 0 1 7 -7 z" fill="var(--orange)"/>
        <circle cx="330" cy="347" r="2.6" fill="var(--white)"/>
        <g class="sans fill-ink" font-size="15">
          <text x="349" y="353">14 Orchard Square Wrexley,</text>
          <text x="349" y="369">Hallamshire WX4 2QP</text>
        </g>

        <circle cx="330" cy="391" r="8" fill="var(--orange)"/>
        <path d="M327 386 c-1 1 -1 3 1 5 l1 1 c2 2 4 2 5 1 l1 -1 -2 -2 -1 1 c-1 0 -3 -2 -3 -3 l1 -1 -2 -2 z" fill="var(--white)"/>
        <text x="349" y="399" class="sans fill-ink" font-size="15">01632 960418</text>

        <circle cx="330" cy="411" r="8" fill="var(--orange)"/>
        <rect x="325" y="407.5" width="10" height="7" fill="none" stroke="var(--white)" stroke-width="1.3"/>
        <path d="M325 408 l5 4 5 -4" fill="none" stroke="var(--white)" stroke-width="1.3"/>
        <text x="349" y="415" class="sans fill-ink" font-size="15">info@brantleyestateagents.co.uk</text>

        <g class="sans heavy fill-orange" font-size="23">
          <text x="340" y="461">Phone lines are open</text>
          <text x="340" y="487">8am to 9pm</text>
          <text x="340" y="512">7 days a week!</text>
        </g>

        <rect x="321" y="554" width="300" height="33" rx="16" fill="var(--black)"/>
        <text x="340" y="578" class="sans heavy fill-white" font-size="22">Follow Us</text>

        <!-- footer swoosh -->
        <path d="M0 780 C250 796 450 755 588 685 V700 C450 770 250 810 0 795 Z" fill="var(--orange)"/>
        <path d="M0 795 C250 810 450 770 588 700 V832 H0 Z" fill="var(--black)"/>

        <!-- photo roundels -->
        <circle cx="391" cy="713" r="74" fill="var(--orange)"/>
        <circle cx="391" cy="713" r="69" fill="url(#keysTones)" role="img" aria-label="Photograph of a hand holding house keys and a small model house"/>
        <circle cx="511" cy="656" r="54" fill="var(--orange)"/>
        <circle cx="511" cy="656" r="49" fill="url(#planTones)" role="img" aria-label="Photograph of a floorplan drawing being worked on"/>
        <circle cx="506" cy="751" r="42" fill="var(--orange)"/>
        <circle cx="506" cy="751" r="37" fill="url(#gemTones)" role="img" aria-label="Photograph of scattered diamonds"/>
      </g>
    </svg>
  </section>

</main>
</body>
</html>
```